Word Cloud Graphic Wallpaper design

The following sentences need to be put together in an ai file of the size : 70" wide and 108" high . This will be used as a wall paper. Inspirational image is attached. (We have also attached a rough idea showing you the wall it would go one- DO NOT REPLICATE THE LAYOUT OF THE SENTENCES-This only shows you how we will be using your file)

Sentences are:

Dentistry is not Expensive Neglect is!
Smiles are free but they are worth alot.
Don't Forget to Floss!
Put on your best SMILE everyday!
Be the reason someone smiles today.
Let your SMILE CHANGE THE WORLD, don't let the world change your smile.
Make your smile your signature accessory!

These should be in different fonts (clean modern fonts only please- no cursive or busy fonts - Helvetica Neue, Arial and fonts such as those are preferred) and sizes and should be easily legible (minimum font height 4"). Repetitions are ok if needed to fill space.

Font styles to use
Sans Serif

Requirements
Must have
• hese should be in different fonts (clean modern fonts only please- no cursive or busy fonts - Helvetica Neue, Arial and fonts such as those) and sizes and should be easily legible (minimum font height 4"). Repetitions are ok if needed to fill space.
Should not have
• Cursive, busy, fonts.

```html
<!DOCTYPE html>
<html lang="en">
<head>
<meta charset="utf-8">
<title>Smile Word Cloud Wallpaper</title>
<link rel="stylesheet" href="https://fonts.googleapis.com/css2?family=Raleway:wght@400;700&family=Ubuntu:wght@700&family=Cardo:wght@400;700&family=Sniglet:wght@400&family=Cinzel:wght@900&family=EB+Garamond:wght@500&display=swap">
<style>
  :root {
    --paper: #ffffff;
    --slate: #5b5b5d;
    --rose: #ea4f6c;
    --honey: #f5bf4e;
    --leaf: #4dae4a;
    --brick: #b6412b;
    --sky: #4a9fc2;
    --tangerine: #f5933f;
  }
  html, body {
    margin: 0;
    padding: 0;
    width: 777px;
    height: 1200px;
    overflow: hidden;
    background: var(--paper);
  }
  .wallpaper {
    position: relative;
    width: 777px;
    height: 1200px;
    overflow: hidden;
    background: var(--paper);
  }
  .cloud {
    position: absolute;
    left: 0;
    top: 0;
    width: 712px;
    height: 1086px;
    transform-origin: 0 0;
    transform: scale(1.0913, 1.105);
  }
  .word {
    position: absolute;
    margin: 0;
    line-height: 1;
    white-space: nowrap;
  }
  .world { font-family: "Raleway", Arial, sans-serif; font-weight: 700; color: var(--slate); }
  .best { font-family: "Ubuntu", Arial, sans-serif; font-weight: 700; color: var(--rose); }
  .dentistry { font-family: "Cardo", Georgia, serif; color: var(--honey); }
  .reason { font-family: "Sniglet", Arial, sans-serif; font-weight: 400; color: var(--leaf); }
  .free { font-family: "Cardo", Georgia, serif; font-weight: 700; color: var(--brick); }
  .signature { font-family: "Cinzel", Georgia, serif; font-weight: 900; color: var(--sky); }
  .signature-thin { font-family: "Raleway", Arial, sans-serif; font-weight: 400; color: var(--sky); letter-spacing: 0.45em; }
  .floss { font-family: "EB Garamond", Georgia, serif; font-weight: 500; color: var(--tangerine); }
</style>
</head>
<body>
<main class="wallpaper">
  <div class="cloud">
    <p class="word world" style="left:22px; top:2px; font-size:62px;">Let your SMILE</p>
    <p class="word world" style="left:12px; top:78px; font-size:56px;">CHANGE THE WORLD,</p>

    <p class="word best" style="left:18px; top:141px; font-size:54px;">Put on</p>
    <p class="word world" style="left:232px; top:152px; font-size:46px;">Don't let the world</p>
    <p class="word best" style="left:14px; top:212px; font-size:64px;">your</p>
    <p class="word dentistry" style="left:180px; top:200px; font-size:70px;">Dentistry</p>
    <p class="word world" style="left:488px; top:202px; font-size:50px;">change</p>
    <p class="word best" style="left:12px; top:262px; font-size:128px;">best</p>
    <p class="word dentistry" style="left:320px; top:276px; font-size:64px;">is</p>
    <p class="word world" style="left:388px; top:275px; font-size:50px;">your smile.</p>
    <p class="word dentistry" style="left:318px; top:345px; font-size:56px;">not expensive</p>
    <p class="word best" style="left:14px; top:392px; font-size:92px;">SMILE</p>
    <p class="word dentistry" style="left:318px; top:405px; font-size:104px;">Neglect</p>
    <p class="word best" style="left:16px; top:472px; font-size:52px;">everyday!</p>

    <p class="word reason" style="left:12px; top:540px; font-size:72px;">Be the</p>
    <p class="word reason" style="left:272px; top:530px; font-size:82px;">reason</p>
    <p class="word dentistry" style="left:588px; top:522px; font-size:88px;">is!</p>

    <p class="word free" style="left:12px; top:636px; font-size:64px;">Smiles</p>
    <p class="word reason" style="left:268px; top:626px; font-size:82px;">someone</p>
    <p class="word free" style="left:12px; top:702px; font-size:60px;">are free</p>
    <p class="word reason" style="left:270px; top:722px; font-size:58px;">smiles today.</p>
    <p class="word free" style="left:12px; top:775px; font-size:60px;">but they</p>
    <p class="word free" style="left:265px; top:800px; font-size:54px;">are worth</p>
    <p class="word free" style="left:558px; top:826px; font-size:58px;">alot.</p>

    <p class="word signature" style="left:10px; top:860px; font-size:38px;">Make your</p>
    <p class="word signature" style="left:268px; top:860px; font-size:38px;">Smile your</p>
    <p class="word signature-thin" style="left:294px; top:900px; font-size:30px;">SIGNATURE</p>
    <p class="word floss" style="left:12px; top:884px; font-size:106px;">Don't</p>
    <p class="word signature" style="left:270px; top:934px; font-size:56px;">Accessory!</p>
    <p class="word floss" style="left:14px; top:990px; font-size:84px;">Forget</p>
    <p class="word floss" style="left:275px; top:990px; font-size:84px;">to Floss!</p>
  </div>
</main>
</body>
</html>
```